Menu Design for Chocolate and Cheese Shop

We are chocolate (and cheese) makers - www.velmarita.com.au and would like to redesign our café menu (attached is the pdf of the old one). I would like to end up with a file using Adobe suite of products so we can readily update menus as we change them. Clean, classy and inviting. We would also like to incorporate our cheese with our sister business into the menu offering (www.dunhollowmead.com.au and www.facebook.com/dunhollowmead). Just allow space for us to flesh out content for the cheese menu items - we will definitely include our Tall Platter in this if you see our facebook posts) - 4pp - A4 landscape folded into A5. We would also like the exact same menu but with our Dunhollow Mead Branding instead of velmarita (we have two different sites -attached are our dunhollow mead logos as well for incorporating into the second document)

```html
<!DOCTYPE html>
<html lang="en">
<head>
<meta charset="utf-8">
<title>Dunhollow Mead — Café Menu</title>
<link href="https://fonts.googleapis.com/css2?family=Libre+Baskerville:ital,wght@0,400;0,700;1,400&family=Playfair+Display:ital,wght@1,400;1,500&display=swap" rel="stylesheet">
<style>
  :root {
    --backdrop: #55514d;
    --paper: #fbf8f3;
    --band: #2d2727;
    --ink: #2a2320;
    --ink-soft: #5a4f48;
    --rule: #7a6e66;
    --brand-red: #c23a2c;
    --white: #ffffff;
    --cheese-cream: #efe4c9;
    --cheese-rind: #d9cdb2;
    --tomato: #b8412e;
    --choc-dark: #3b261c;
    --choc-mid: #6e4630;
    --cacao-gold: #c08a3a;
    --wood: #8a5a35;
    --serif: "Libre Baskerville", Georgia, serif;
    --script: "Playfair Display", Georgia, serif;
  }
  * { box-sizing: border-box; margin: 0; padding: 0; }
  html, body { width: 1200px; height: 2553px; overflow: hidden; }
  body {
    background: var(--backdrop);
    font-family: var(--serif);
    color: var(--ink);
    position: relative;
  }

  /* ---------- sheets ---------- */
  .sheet {
    position: absolute;
    height: 720px;
    background: var(--paper);
    box-shadow: 0 18px 40px rgba(0,0,0,.35);
    overflow: hidden;
  }
  .sheet--single { width: 510px; left: 345px; top: 70px; }
  .sheet--inside { width: 1020px; left: 90px; top: 900px; display: flex; }
  .sheet--outside { width: 1020px; left: 90px; top: 1730px; display: flex; }
  .page { position: relative; width: 510px; height: 720px; }
  .sheet--inside .page + .page,
  .sheet--outside .page + .page { border-left: 1px solid rgba(0,0,0,.08); }

  /* ---------- cover ---------- */
  .cover { position: relative; width: 510px; height: 720px; background: var(--white); }
  .cover-photo { position: absolute; }
  .cover-photo--cheese {
    left: 0; top: 0; width: 232px; height: 270px;
    background: linear-gradient(150deg, var(--tomato) 0%, #c98e6a 18%, var(--cheese-cream) 45%, var(--cheese-rind) 75%, #8f7a5f 100%);
  }
  .cover-photo--bark {
    left: 240px; top: 0; width: 270px; height: 270px;
    background: linear-gradient(200deg, #e8ddc8 0%, #b08a5e 30%, var(--choc-mid) 55%, var(--choc-dark) 100%);
  }
  .cover-band {
    position: absolute; left: 0; top: 278px; width: 510px; height: 150px;
    background: var(--band);
    display: flex; flex-direction: column; align-items: center; justify-content: center;
    color: var(--white); gap: 10px;
  }
  .brand {
    display: flex; align-items: center; gap: 10px;
    font-family: var(--serif); font-weight: 700;
    letter-spacing: .06em; text-transform: uppercase;
  }
  .brand-dot { width: 10px; height: 10px; border-radius: 50%; background: currentColor; }
  .cover-band .brand { font-size: 24px; }
  .cover-tagline {
    font-size: 9px; letter-spacing: .22em; text-transform: uppercase;
    text-align: center; line-height: 1.7; opacity: .9;
  }
  .cover-photo--jars {
    left: 0; top: 436px; width: 300px; height: 284px;
    background: linear-gradient(160deg, var(--wood) 0%, #b88a5a 35%, #e9e2d6 60%, #d8cfc0 100%);
  }
  .cover-photo--cacao {
    left: 308px; top: 436px; width: 202px; height: 284px;
    background: linear-gradient(135deg, var(--choc-dark) 0%, var(--choc-mid) 30%, var(--cacao-gold) 55%, #8b6a4c 75%, var(--choc-dark) 100%);
  }

  /* ---------- menu type ---------- */
  .menu-photo { position: absolute; inset: 0; }
  .menu-photo--cacao-hands {
    background:
      radial-gradient(ellipse 260px 200px at 600px 340px, rgba(196,150,80,.75), transparent 70%),
      radial-gradient(ellipse 220px 260px at 870px 470px, rgba(120,80,60,.55), transparent 70%),
      radial-gradient(ellipse 300px 240px at 330px 330px, rgba(230,200,150,.55), transparent 70%),
      linear-gradient(90deg, #f3ece0 0%, #efe3cf 40%, #e6d6bb 60%, #d7dcd6 100%);
  }
  .menu-photo--cheese-board {
    background:
      radial-gradient(ellipse 140px 40px at 330px 440px, rgba(90,130,60,.45), transparent 70%),
      radial-gradient(ellipse 300px 200px at 240px 560px, rgba(240,236,226,.9), transparent 70%),
      linear-gradient(180deg, #ece9e3 0%, #dedad3 55%, #cdbfa9 100%);
  }
  .menu-column { position: absolute; inset: 34px 40px 30px 40px; }
  .menu-heading {
    display: flex; align-items: center; gap: 14px;
    font-family: var(--script); font-style: italic; font-weight: 400;
    font-size: 24px; color: var(--ink); margin-bottom: 14px;
  }
  .menu-heading::after { content: ""; flex: 1; max-width: 120px; height: 1px; background: var(--rule); }
  .menu-item { margin-bottom: 10px; }
  .menu-item-name { font-size: 11.5px; font-weight: 700; line-height: 1.35; }
  .menu-item-desc { font-size: 9.5px; line-height: 1.5; color: var(--ink-soft); }

  .kids-box {
    position: absolute; left: 40px; right: 40px; bottom: 50px;
    border: 1px solid var(--rule); padding: 16px 20px 18px;
    background: rgba(255,255,255,.35);
  }
  .kids-box .menu-heading { font-size: 20px; margin-bottom: 10px; }
  .kids-list { display: grid; grid-template-columns: 1fr 1fr; }
  .kids-list ul { list-style: none; font-size: 10.5px; font-weight: 700; line-height: 2; }
  .kids-list ul + ul { border-left: 1px dotted var(--rule); padding-left: 16px; }

  .dotted-rule { border-top: 2px dotted var(--ink); width: 300px; margin: 18px 0 0; }
  .contact-card {
    position: absolute; left: 40px; bottom: 46px; width: 330px; height: 150px;
    background: rgba(251,246,232,.88);
    display: flex; flex-direction: column; align-items: center; justify-content: center;
    gap: 4px; text-align: center;
  }
  .contact-card .brand { color: var(--brand-red); font-size: 17px; margin-bottom: 8px; }
  .contact-card p { font-size: 9.5px; line-height: 1.5; }
</style>
</head>
<body>

<!-- Front cover -->
<section class="sheet sheet--single" aria-label="Front cover">
  <div class="cover">
    <div class="cover-photo cover-photo--cheese" role="img" aria-label="Photo of soft and blue cheeses with cherry tomatoes"></div>
    <div class="cover-photo cover-photo--bark" role="img" aria-label="Photo of chocolate bark topped with fruit and nuts"></div>
    <div class="cover-band">
      <div class="brand"><span class="brand-dot"></span>Dunhollow Mead</div>
      <p class="cover-tagline">Cheese, chocolate,<br>goat feeding &amp; fig wrangling</p>
    </div>
    <div class="cover-photo cover-photo--jars" role="img" aria-label="Photo of wrapped cheese rounds and jars on a wooden table"></div>
    <div class="cover-photo cover-photo--cacao" role="img" aria-label="Photo of split cacao pods, cocoa beans and chocolate squares"></div>
  </div>
</section>

<!-- Inside spread -->
<section class="sheet sheet--inside" aria-label="Inside spread">
  <div class="menu-photo menu-photo--cacao-hands" role="img" aria-label="Faded photo of hands holding an opened cacao pod"></div>

  <div class="page">
    <div class="menu-column">
      <h2 class="menu-heading">Sweet Treats</h2>
      <div class="menu-item"><p class="menu-item-name">Chocolate Taste Plate - $14.50</p><p class="menu-item-desc">Chocolate mousse, chocolate ice cream, chocolate truffle and our signature chocolate</p></div>
      <div class="menu-item"><p class="menu-item-name">Caramel Taste Plate - $14.50</p><p class="menu-item-desc">Caramel slice, baked caramel, caramel truffle, and shortbread filled with dulce de leche</p></div>
      <div class="menu-item"><p class="menu-item-name">Raspberry Brownie - $11.50</p><p class="menu-item-desc">Brownie topped with raspberries, served warm with a scoop of vanilla bean ice cream</p></div>
      <div class="menu-item"><p class="menu-item-name">Ice-cream Sensation - $12.00</p><p class="menu-item-desc">A trio of chocolate ice cream or our weekly special ice cream served with chocolate sauce and sprinkled with dark crispy pearls. Ask our team what flavour is available</p></div>
      <div class="menu-item"><p class="menu-item-name">Chocolate Mousse - $12.00</p><p class="menu-item-desc">Rich and creamy chocolate mousse served with white crispy pearls</p></div>
      <div class="menu-item"><p class="menu-item-name">Dessert Jars - $13.50</p><p class="menu-item-desc">Ask our team to find out what is on offer this week</p></div>
      <div class="menu-item"><p class="menu-item-name">Handmade Cookies - $3.00</p></div>
    </div>
    <div class="kids-box">
      <h3 class="menu-heading">For the Children</h3>
      <div class="kids-list">
        <ul><li>Mini hot chocolate - $3.50</li><li>Mini chinos - $1.50</li><li>Mini chinos with teddy pop - $2.50</li></ul>
        <ul><li>Mini ice chocolate - $6.00</li><li>Mini icecream - $3.50</li><li>Mini mousse - $3.50</li></ul>
      </div>
    </div>
  </div>

  <div class="page">
    <div class="menu-column">
      <h2 class="menu-heading">Drinks</h2>
      <div class="menu-item"><p class="menu-item-name">Hot Chocolate - Reg $5.50 - Lrg $6.00</p><p class="menu-item-desc">Traditional – made with 70% Venezuelan single origin chocolate. White – made with white chocolate. Half and half – half traditional and half white hot chocolate</p></div>
      <div class="menu-item"><p class="menu-item-name">Mocha - Reg $6.00 - Lrg $6.50</p><p class="menu-item-desc">Can be made with traditional or white chocolate</p></div>
      <div class="menu-item"><p class="menu-item-name">Special Hot Chocolate - Reg $6.50 - Lrg $7.00</p><p class="menu-item-desc">A creamy ganache made with cream &amp; butter infused with a different flavour each week (ask our team what flavour is available)</p></div>
      <div class="menu-item"><p class="menu-item-name">Coffee - Reg $4.00 - Lrg $4.50</p><p class="menu-item-desc">Latte, cappuccino, flat white, long black, short black, short macchiato, long macchiato, piccolo latte</p></div>
      <div class="menu-item"><p class="menu-item-name">Chai - Reg $4.00 - Lrg $4.50</p></div>
      <div class="menu-item"><p class="menu-item-name">Tea - A pot of Leafwell organic tea - $5.00</p><p class="menu-item-desc">English breakfast, earl grey, french earl grey, wellbeing, coconut, berry, green, white tea and roses, chai, dark tea &amp; chocolate, lemongrass and ginger</p></div>
      <div class="menu-item"><p class="menu-item-name">Affogato - $6.00</p><p class="menu-item-desc">Vanilla bean ice cream served with a shot of coffee or molten chocolate</p></div>
      <div class="menu-item"><p class="menu-item-name">Iced Coffee - $5.50</p></div>
      <div class="menu-item"><p class="menu-item-name">Iced Chocolate - $7.00 - White or 65% Maracaibo Single Origin Chocolate</p><p class="menu-item-desc">Our special blend of iced cream, milk, and chocolate</p></div>
      <div class="menu-item"><p class="menu-item-name">Iced Mocha - White or Traditional - $7.50</p></div>
      <div class="menu-item"><p class="menu-item-name">Milkshakes - $6.00</p><p class="menu-item-desc">Chocolate, your own decadent fudge, vanilla or caramel</p></div>
      <div class="menu-item"><p class="menu-item-name">Linford - Still or Sparkling Water $3.00</p></div>
    </div>
  </div>
</section>

<!-- Outside spread: back page and front cover -->
<section class="sheet sheet--outside" aria-label="Outside spread">
  <div class="page">
    <div class="menu-photo menu-photo--cheese-board" role="img" aria-label="Soft-focus photo of fresh cheese with basil leaves"></div>
    <div class="menu-column">
      <h2 class="menu-heading">Cheese Menu</h2>
      <div class="menu-item"><p class="menu-item-name">The Rat Trap Sandwich - $0.00</p><p class="menu-item-desc">Aged cheddar, house pickle and rocket on toasted sourdough.</p></div>
      <div class="menu-item"><p class="menu-item-name">Poutine - $0.00</p><p class="menu-item-desc">Crisp chips, fresh curds and rich gravy, finished with herbs.</p></div>
      <div class="menu-item"><p class="menu-item-name">Mac and Cheese - $00.00</p><p class="menu-item-desc">Baked macaroni in a three cheese sauce with a golden crumb.</p></div>
      <div class="menu-item"><p class="menu-item-name">Cheese Omelette - $00.00</p><p class="menu-item-desc">Three eggs folded with washed rind cheese and chives.</p></div>
      <div class="menu-item"><p class="menu-item-name">Caprese Grilled Cheese - $00.00</p><p class="menu-item-desc">Buffalo mozzarella, tomato and basil pressed in sourdough.</p></div>
      <div class="menu-item"><p class="menu-item-name">Sweet Goat Salad - $00.00</p><p class="menu-item-desc">Fresh goat curd, figs and leaves with honey dressing.</p></div>
      <div class="dotted-rule"></div>
    </div>
    <div class="contact-card">
      <div class="brand"><span class="brand-dot"></span>Dunhollow Mead</div>
      <p>1800 402 716</p>
      <p>e: hello@dunhollowmead.com.au</p>
      <p>Dunhollow Mead</p>
      <p>ABN 52 804 317 926</p>
    </div>
  </div>

  <div class="page">
    <div class="cover">
      <div class="cover-photo cover-photo--cheese" role="img" aria-label="Photo of soft and blue cheeses with cherry tomatoes"></div>
      <div class="cover-photo cover-photo--bark" role="img" aria-label="Photo of chocolate bark topped with fruit and nuts"></div>
      <div class="cover-band">
        <div class="brand"><span class="brand-dot"></span>Dunhollow Mead</div>
        <p class="cover-tagline">Cheese, chocolate,<br>goat feeding &amp; fig wrangling</p>
      </div>
      <div class="cover-photo cover-photo--jars" role="img" aria-label="Photo of wrapped cheese rounds and jars on a wooden table"></div>
      <div class="cover-photo cover-photo--cacao" role="img" aria-label="Photo of split cacao pods, cocoa beans and chocolate squares"></div>
    </div>
  </div>
</section>

</body>
</html>
```